Business Card Design

I am a Accounting/Bookkeeping company.  As a sideline, I am also a Notary so I would like that somewhere, either in front or perhaps the backside for the notary business.
I found a standard card I really like but didn't like the "little man" standing on the scale.
I love the colors so I am wondering if you would be able to duplicate this without the man and perhaps money or something appropriate on this side of scale
I also need help on the font.  I tend to like feminine styles but am told they are too hard to read.

Target Market(s)
Small businesses, Individuals
Industry/Entity Type
Business
Contact Information for Business Card
The Tidy Ledgerwright
Balancing your books is our specialty
Marisol (Pebbleton) Varnaccio
Accounting Associate
Certified FiscalTrail CountExpert
Notary Public
Serving Sonoma County                            415-362-9184
marisol.varnaccio@plumpost.example

Requirements
Must have
- I would like a glossy card

```html
<!DOCTYPE html>
<html lang="en">
<head>
<meta charset="utf-8">
<title>The Tidy Ledgerwright – Business Card</title>
<link rel="stylesheet" href="https://fonts.googleapis.com/css2?family=Macondo&family=Forum&family=Gelasio&display=swap">
<style>
  :root {
    --page-bg: #efefef;
    --card-olive: #8b8a38;
    --band-black: #050505;
    --ink-white: #ffffff;
    --ink-black: #111111;
    --scale-light: #d6d6d6;
    --scale-dark: #1a1a1a;
  }
  * { box-sizing: border-box; margin: 0; padding: 0; }
  html, body {
    width: 1200px; height: 1000px; overflow: hidden;
    background: var(--page-bg);
  }
  .card {
    position: absolute; left: 305px; top: 320px;
    width: 572px; height: 317px;
    background: var(--card-olive);
    overflow: hidden;
  }
  .brand-name {
    position: absolute; left: 0; width: 544px; top: 22px;
    text-align: center;
    font-family: "Macondo", cursive;
    font-size: 23px; letter-spacing: 1.5px;
    color: var(--ink-white);
  }
  .tagline {
    position: absolute; left: 222px; top: 47px;
    font-family: "Forum", serif;
    font-size: 12px; letter-spacing: 0.6px;
    text-transform: uppercase;
    color: var(--ink-black);
  }
  .person-name {
    position: absolute; left: 40px; top: 117px;
    font-family: "Macondo", cursive;
    font-size: 20px; letter-spacing: 0.5px;
    font-variant: small-caps;
    color: var(--ink-white);
  }
  .credentials {
    position: absolute; left: 40px; width: 310px; top: 145px;
    text-align: center;
    font-family: "Gelasio", serif;
    font-size: 14.5px; line-height: 19px;
    color: var(--ink-black);
  }
  .scale-art {
    position: absolute; left: 372px; top: 124px;
    width: 164px; height: 116px;
  }
  .info-cell {
    position: absolute;
    background: var(--band-black);
    color: var(--ink-white);
    display: flex; align-items: center; justify-content: center;
    white-space: nowrap;
  }
  .row-top { top: 239px; height: 25px; }
  .row-bottom { top: 269px; height: 20px; }
  .col-left { left: 0; width: 251px; }
  .col-right { left: 256px; width: 316px; }
  .notary {
    font-family: "Macondo", cursive; font-size: 14px; letter-spacing: 1px;
  }
  .service-area {
    font-family: "Forum", serif; font-size: 15px; letter-spacing: 0.4px;
    font-variant: small-caps;
  }
  .phone {
    font-family: "Macondo", cursive; font-size: 14px; letter-spacing: 1px;
  }
  .email {
    font-family: "Forum", serif; font-size: 12.5px; letter-spacing: 0.6px;
    text-transform: uppercase;
  }
</style>
</head>
<body>
  <main class="card">
    <h1 class="brand-name">The Tidy Ledgerwright</h1>
    <p class="tagline">Balancing your books is our specialty</p>

    <h2 class="person-name">Marisol (Pebbleton) Varnaccio</h2>
    <p class="credentials">Accounting Associate<br>Certified FiscalTrail CountExpert</p>

    <svg class="scale-art" viewBox="0 0 164 116" role="img" aria-label="Illustration of a balance scale with books on one pan and a dollar sign on the other">
      <defs>
        <linearGradient id="scaleTone" x1="0" y1="0" x2="0" y2="1">
          <stop offset="0" stop-color="var(--scale-light)"/>
          <stop offset="1" stop-color="var(--scale-dark)"/>
        </linearGradient>
      </defs>
      <rect width="164" height="116" rx="6" fill="url(#scaleTone)" opacity="0.55"/>
    </svg>

    <div class="info-cell row-top col-left notary">Notary Public</div>
    <div class="info-cell row-top col-right phone">415-362-9184</div>
    <div class="info-cell row-bottom col-left service-area">Serving Sonoma County</div>
    <div class="info-cell row-bottom col-right email">marisol.varnaccio@plumpost.example</div>
  </main>
</body>
</html>
```